BRAVO (Bright Regional Applied Vector Operations) Letter Head Design Project

Company Name: BRAVO (Bright Regional Applied Vector Operations) MFZ.
Office Address: Office No 718, Saffron Crest Block, Palmera Garden Quarter, Dubai, U.A.E
Company line of business:
1) Currently we have a POS solution for retail outlets like duty free shops, supermarkets, department stores etc... The solution is deployed in Harbourline Travel Retail on 350 POS and in Corniche Gate Travel Retail on 100 POS. So our main line of business is the deployment of this solution in retail outlets locally or regionally. We have already deployed the solution in India and Australia.
2) Integration of other third party POS systems with an online credit authorization netwotk in the UAE. This will enable POS applications to connect directly to the acquiring banks without needing an EFT terminal like Paxomat or Tallyrex. The credit card payment is completed at the POS.
3) Other solutions that are targeting retail outlets like mobile POS, queue busting solutions, stock taking solutions using hand held devices, transaction capture systems, etc...
4) Other IT services like support of call center solutions from Bluegrove Systems and development of new solutions as per customer requirements.
We need a letter head design for the company. We don't have any specific requirements in mind and we prefer to leave it up to the designers to come up with creative designs that will not be limited by any guidelines.
Updates
I have just uploaded all the files I received from my company logo designer. Please review and let me know if you need anything else. .
Dear All,
I have received very nice designs and I thank you for all the hard work you have put so far. I would like the letter head to have all the following company details:
Office Address: Office No 718, Saffron Crest Block, MFZ, Dubai UAE
P.O.Box: 58316 Dubai UAE
Tel Number:+971-4-5817730
Fax Number::+971-4-5817731
Website:www.bravomfz.ae
I would also like to represent the company details as a QRCode somewhere on the page, probably next to the company details if possible (as a trial).
In case you have included a butterfly in the middle of the page as part of your design, I prefer that it doesn't include any colors as colors might make reading the text on the page more difficult.
I don't want to have too many butterflies on the page. 2 are more than enough.
Can you also include a design for the continuation pages?
Thank you in advance and I look forward to receiving your creative designs.
Regards
Samir Odeyra

```html
<!DOCTYPE html>
<html lang="en">
<head>
<meta charset="utf-8">
<title>BRAVO Letterhead</title>
<link href="https://fonts.googleapis.com/css2?family=Bebas+Neue&family=Open+Sans:wght@400&display=swap" rel="stylesheet">
<style>
  :root {
    --brand-blue: #359fd8;
    --title-grey: #8a8a8a;
    --paper: #ffffff;
    --ghost: #f6f6f6;
    --ghost-text: #f0f0f0;
    --footer-text: #ffffff;
  }
  html, body {
    margin: 0;
    padding: 0;
    overflow: hidden;
    background: var(--paper);
  }
  .letterhead {
    position: relative;
    width: 848px;
    height: 1200px;
    background: var(--paper);
    overflow: hidden;
  }
  .brand-dot {
    position: absolute;
    left: 10px;
    top: 10px;
    width: 94px;
    height: 94px;
    border-radius: 50%;
    background: var(--brand-blue);
  }
  .brand-name {
    position: absolute;
    left: 116px;
    top: 40px;
    margin: 0;
    font-family: "Bebas Neue", "Arial Narrow", sans-serif;
    font-weight: 400;
    font-size: 35px;
    line-height: 1;
    letter-spacing: 0.5px;
    color: var(--title-grey);
    white-space: nowrap;
  }
  .header-rule {
    position: absolute;
    left: 106px;
    top: 85px;
    width: 733px;
    height: 2px;
    background: var(--brand-blue);
  }
  .ghost-mark {
    position: absolute;
    left: 144px;
    top: 425px;
    width: 350px;
    height: 350px;
    border-radius: 50%;
    background: var(--ghost);
  }
  .ghost-name {
    position: absolute;
    left: 250px;
    top: 530px;
    margin: 0;
    font-family: "Bebas Neue", "Arial Narrow", sans-serif;
    font-size: 150px;
    line-height: 1;
    color: var(--ghost-text);
    white-space: nowrap;
  }
  .footer-band {
    position: absolute;
    left: 8px;
    top: 1095px;
    width: 832px;
    height: 97px;
    background: var(--brand-blue);
  }
  .footer-rule {
    position: absolute;
    left: 0;
    top: 24px;
    width: 100%;
    height: 1px;
    background: rgba(255, 255, 255, 0.85);
  }
  .footer-details {
    position: absolute;
    left: 596px;
    top: 0;
    width: 228px;
    height: 100%;
  }
  .footer-company,
  .footer-address {
    position: absolute;
    left: 0;
    margin: 0;
    font-family: "Open Sans", Arial, sans-serif;
    font-size: 10.5px;
    color: var(--footer-text);
    font-style: normal;
  }
  .footer-company {
    top: 6px;
    white-space: nowrap;
  }
  .footer-address {
    top: 31px;
    line-height: 15.5px;
  }
</style>
</head>
<body>
  <main class="letterhead">
    <header>
      <div class="brand-dot"></div>
      <h1 class="brand-name">Bright Regional Applied Vector Operations</h1>
      <div class="header-rule"></div>
    </header>

    <div class="ghost-mark" aria-hidden="true"></div>
    <p class="ghost-name" aria-hidden="true">BRAVO</p>

    <footer class="footer-band">
      <div class="footer-rule"></div>
      <div class="footer-details">
        <p class="footer-company">Bright Regional Applied Vector Operations</p>
        <address class="footer-address">
          Office No 718,<br>
          Saffron Crest Block,<br>
          Palmera Garden Quarter,<br>
          Dubai, U.A.E
        </address>
      </div>
    </footer>
  </main>
</body>
</html>
```